Flyer-Design für Verlegung von fugenlosen Böden
Zielgruppe
Die Firma KORVAL, hat seinen Hauptaugenmerk auf das verlegen von fugenlosen Böden gelegt.
welchen Vorteil bietet Ihnen dieser Bodenbelag? Der fugenlose Bodenbelag wie der Epoxidharzboden oder der Steinteppich ist in den letzten Jahren eine beliebte Alternative zu Laminat, Fliesen, Parkett und anderen Bodenbelägen geworden.Seine steigende Beliebtheit verdankt der fugenlose Bodenbelag unter anderem seiner Robustheit.Unsere Bodenbeläge sind Geruchsneutral und bietet eine lange Lebensdauer. Die Zielgruppe sind Private sowie Gewerbliche Kunden.
Aufgabenstellung
Der Text sollte den effekt, 'Wow' das muss ich haben beim Leser auslösen. Das gleiche zählt für die verwendeten Bilder die der Desinger gerne auswählen derf. Mehr Infos Z.b Logo kann sich der Desinger auf der Webseite entnehmen.
www.korval-estrich.example

```html
<!DOCTYPE html>
<html lang="de">
<head>
<meta charset="utf-8">
<title>KORVAL – Fugenlose Bodenbeläge</title>
<link href="https://fonts.googleapis.com/css2?family=Source+Sans+3:wght@400;600;700&display=swap" rel="stylesheet">
<style>
  :root {
    --orange: #c84a06;
    --text-dark: #4b5059;
    --contact: #1e2126;
    --white: #ffffff;
    --panel: rgba(236, 238, 242, 0.72);
  }
  * { margin: 0; padding: 0; box-sizing: border-box; }
  html, body { width: 1200px; height: 846px; overflow: hidden; background: #fff; }
  .flyer {
    position: relative;
    width: 1200px;
    height: 846px;
    font-family: "Source Sans 3", "Myriad Pro", sans-serif;
  }
  .floor-photo {
    position: absolute;
    left: 0; top: 0;
    width: 832px; height: 846px;
    background:
      linear-gradient(180deg, #dcdcd8 0%, #c9ccce 22%, #a9b8c8 45%, #8fa1b7 70%, #7e8ea6 100%);
  }
  .intro-box {
    position: absolute;
    left: 46px; top: 39px;
    width: 751px; height: 462px;
    background: var(--panel);
    padding: 14px 10px 0 11px;
  }
  .intro-title {
    color: var(--orange);
    font-size: 26px;
    font-weight: 600;
    line-height: 1.2;
    margin-bottom: 26px;
  }
  .intro-text {
    color: var(--text-dark);
    font-size: 21px;
    line-height: 29px;
    margin-bottom: 29px;
  }
  .brand {
    position: absolute;
    left: 64px; top: 600px;
    display: flex;
    align-items: center;
    gap: 14px;
  }
  .brand-mark {
    width: 26px; height: 26px;
    background: var(--orange);
  }
  .brand-name {
    font-size: 54px;
    font-weight: 700;
    letter-spacing: 4px;
    color: #3f454c;
    line-height: 1;
  }
  .contact {
    position: absolute;
    left: 68px; top: 713px;
    color: var(--contact);
    font-size: 21px;
    line-height: 29px;
  }
  .benefits-panel {
    position: absolute;
    left: 832px; top: 0;
    width: 368px; height: 846px;
    background: var(--orange);
  }
  .benefit {
    position: absolute;
    left: 30px;
    display: flex;
    align-items: flex-start;
    color: var(--white);
    font-size: 23px;
    line-height: 29px;
  }
  .benefit svg {
    flex: none;
    width: 46px; height: 40px;
    margin-right: 18px;
  }
  .benefit p { width: 250px; }
</style>
</head>
<body>
<div class="flyer">
  <div class="floor-photo" role="img" aria-label="Foto eines Raums mit grau-blauem fugenlosem Boden und hellen Wänden"></div>

  <section class="intro-box">
    <h1 class="intro-title">Warum ein fugenloser Boden?</h1>
    <p class="intro-text">Je mehr unterschiedliche Materialien als Fußbodenbelag eingesetzt werden, desto kleiner und unruhiger wirkt das gesamte Interieur. Der durchgehende, fugenlose Boden hingegen hält sich elegant im Hin­tergrund und schafft eine ruhige Atmosphäre. Keine ablenkenden Muster oder Absätze stören das Bild, wodurch kleine Räume größer wirken. Besonders toll kommt das auch in offenen Küchen mit anschließendem Wohn-Ess-Bereich zur Geltung.</p>
    <p class="intro-text">Einer der wichtigsten Vorteile gegenüber vielen anderen Bodenbelägen ist, dass der fugenlose Boden besonders robust und leicht zu pflegen ist. Er wird mit mehreren Schichten versiegelt und hat keine störenden Fugen. Anders als bei Parkett, Laminat ,Fliesen oder Vinyl ist er unempfindlich gegen Kratzer und Stöße.</p>
  </section>

  <div class="brand">
    <span class="brand-mark"></span>
    <span class="brand-name">KORVAL</span>
  </div>

  <address class="contact" style="font-style:normal">
    Lindenhang 12 &nbsp;|&nbsp; 66999 Talbrück<br>
    Tel.: 06999-5550123 | Mobil: 0170 - 55 50 19 8<br>
    email: fugenlos@korval-estrich.example &nbsp;|&nbsp; korval-estrich.example
  </address>

  <aside class="benefits-panel">
    <div class="benefit" style="top:86px">
      <svg viewBox="0 0 46 40"><circle cx="20" cy="21" r="17" fill="none" stroke="#fff" stroke-width="3.5"/><path d="M11 20 L19 29 L44 4" fill="none" stroke="#fff" stroke-width="4" stroke-linecap="round" stroke-linejoin="round"/></svg>
      <p>Dem Design sind keine Grenzen gesetzt</p>
    </div>
    <div class="benefit" style="top:174px">
      <svg viewBox="0 0 46 40"><circle cx="20" cy="21" r="17" fill="none" stroke="#fff" stroke-width="3.5"/><path d="M11 20 L19 29 L44 4" fill="none" stroke="#fff" stroke-width="4" stroke-linecap="round" stroke-linejoin="round"/></svg>
      <p>Freie Farbauswahl aus über 200 Farben (metallic,matt)</p>
    </div>
    <div class="benefit" style="top:290px">
      <svg viewBox="0 0 46 40"><circle cx="20" cy="21" r="17" fill="none" stroke="#fff" stroke-width="3.5"/><path d="M11 20 L19 29 L44 4" fill="none" stroke="#fff" stroke-width="4" stroke-linecap="round" stroke-linejoin="round"/></svg>
      <p>Ihr Persönliches Einzelstück</p>
    </div>
    <div class="benefit" style="top:377px">
      <svg viewBox="0 0 46 40"><circle cx="20" cy="21" r="17" fill="none" stroke="#fff" stroke-width="3.5"/><path d="M11 20 L19 29 L44 4" fill="none" stroke="#fff" stroke-width="4" stroke-linecap="round" stroke-linejoin="round"/></svg>
      <p>Weil Ihr Boden kein Standart Boden werden soll!</p>
    </div>
    <div class="benefit" style="top:493px">
      <svg viewBox="0 0 46 40"><circle cx="20" cy="21" r="17" fill="none" stroke="#fff" stroke-width="3.5"/><path d="M11 20 L19 29 L44 4" fill="none" stroke="#fff" stroke-width="4" stroke-linecap="round" stroke-linejoin="round"/></svg>
      <p>Der Boden mit dem Wow Effekt!</p>
    </div>
    <div class="benefit" style="top:580px">
      <svg viewBox="0 0 46 40"><circle cx="20" cy="21" r="17" fill="none" stroke="#fff" stroke-width="3.5"/><path d="M11 20 L19 29 L44 4" fill="none" stroke="#fff" stroke-width="4" stroke-linecap="round" stroke-linejoin="round"/></svg>
      <p>Geben Sie sich nicht mit weniger zufrieden!</p>
    </div>
    <div class="benefit" style="top:667px">
      <svg viewBox="0 0 46 40"><circle cx="20" cy="21" r="17" fill="none" stroke="#fff" stroke-width="3.5"/><path d="M11 20 L19 29 L44 4" fill="none" stroke="#fff" stroke-width="4" stroke-linecap="round" stroke-linejoin="round"/></svg>
      <p>Hochglanz &nbsp;oder Matt Versiegelung</p>
    </div>
  </aside>
</div>
</body>
</html>
```